I need a business card to reflect my new qualifications.
Accredited Teacher, Accredited Valuer & Accredited Judge of Patchwork Quilting.
Fernbrook Lane Studio
47 Harlow Parade, Elmsford Vic 3712
0417 362 958 fernbrook@qlx.com.au

```html
<!DOCTYPE html>
<html lang="en">
<head>
<meta charset="utf-8">
<title>Fernbrook Lane Studio – Business Card</title>
<link rel="stylesheet" href="https://fonts.googleapis.com/css2?family=Zilla+Slab:wght@300;400&display=swap">
<style>
  :root {
    --stage: #2b2b2d;
    --denim: #5b5a80;
    --denim-deep: #4a4868;
    --panel: #46445f;
    --pink: #d9427c;
    --pink-soft: #f08ab0;
    --patch-red: #c8325f;
    --patch-rose: #e87aa2;
    --patch-teal: #6fb7c4;
    --patch-wine: #8e2446;
    --ink-light: #ecebf3;
  }
  * { box-sizing: border-box; margin: 0; padding: 0; }
  html, body { width: 1200px; height: 900px; overflow: hidden; }
  body {
    background: var(--stage);
    font-family: "Zilla Slab", Georgia, serif;
    font-weight: 300;
    position: relative;
  }
  .card {
    position: absolute;
    left: 320px;
    width: 560px;
    height: 320px;
    border-radius: 14px;
    overflow: hidden;
    background: radial-gradient(ellipse at 50% 50%, #66658c 0%, var(--denim) 55%, var(--denim-deep) 100%);
    box-shadow: 0 18px 40px rgba(0,0,0,.55);
  }
  .card--front { top: 100px; }
  .card--back { top: 480px; }

  .patchwork {
    position: absolute;
    background: linear-gradient(90deg, var(--patch-rose), var(--patch-red) 30%, var(--patch-teal) 55%, var(--patch-wine) 80%, var(--patch-rose));
    opacity: .85;
  }
  .front-patch--top { top: 0; right: 0; width: 300px; height: 60px; border-bottom-left-radius: 40px; }
  .front-patch--right { top: 60px; right: 0; width: 50px; height: 130px; }
  .front-patch--bottom { bottom: 0; left: 0; width: 100%; height: 56px; }
  .front-patch--left { top: 170px; left: 0; width: 50px; height: 94px; }

  .front-name {
    position: absolute;
    left: 60px; right: 60px; top: 130px;
    text-align: center;
    font-size: 36px;
    font-weight: 300;
    letter-spacing: 2px;
    color: var(--ink-light);
  }

  .back-patch--top { top: 0; left: 0; width: 100%; height: 78px; }
  .back-patch--right { top: 78px; right: 0; width: 50px; height: 100px; }
  .back-patch--bottom { bottom: 0; left: 220px; width: 220px; height: 36px; }

  .info-panel {
    position: absolute;
    left: 0; top: 78px;
    width: 510px; height: 206px;
    background: var(--panel);
  }
  .qualifications {
    position: absolute;
    left: 26px; top: 12px;
    width: 460px;
    font-size: 15px;
    line-height: 1.25;
    color: var(--ink-light);
  }
  .identity {
    position: absolute;
    left: 0; top: 66px;
    width: 250px; height: 110px;
    background: var(--pink);
    padding: 14px 0 0 26px;
  }
  .identity__name { font-size: 19px; color: var(--ink-light); }
  .identity__studio { font-size: 17px; color: var(--pink-soft); margin-top: 10px; }

  .pointer { position: absolute; left: 254px; width: 18px; height: 10px; }
  .pointer--one { top: 70px; }
  .pointer--two { top: 102px; }

  .contacts {
    position: absolute;
    left: 288px; top: 64px;
    list-style: none;
    font-size: 14px;
    color: var(--ink-light);
  }
  .contacts li { display: flex; align-items: flex-start; gap: 10px; margin-bottom: 10px; line-height: 1.2; }
  .contacts svg { width: 12px; height: 12px; margin-top: 2px; flex: none; }
</style>
</head>
<body>

<section class="card card--front" aria-label="Card front">
  <div class="patchwork front-patch--top" role="img" aria-label="Patchwork quilt fabric squares in pinks and teal"></div>
  <div class="patchwork front-patch--right" role="img" aria-label="Patchwork quilt fabric squares"></div>
  <div class="patchwork front-patch--left" role="img" aria-label="Patchwork quilt fabric squares"></div>
  <div class="patchwork front-patch--bottom" role="img" aria-label="Row of patchwork quilt fabric squares"></div>
  <p class="front-name">Fernbrook Lane Studio</p>
</section>

<section class="card card--back" aria-label="Card back">
  <div class="patchwork back-patch--top" role="img" aria-label="Row of patchwork quilt fabric squares"></div>
  <div class="patchwork back-patch--right" role="img" aria-label="Patchwork quilt fabric squares"></div>

  <div class="info-panel">
    <p class="qualifications">Accredited Teacher, Accredited<br>Valuer &amp; Accredited Judge of Patchwork Quilting</p>

    <div class="identity">
      <p class="identity__name">Helen Ashcombe</p>
      <p class="identity__studio">Fernbrook Lane Studio</p>
    </div>

    <svg class="pointer pointer--one" viewBox="0 0 18 10"><path d="M1 1 L9 5 L1 9 M9 5 H17" fill="none" stroke="#d9427c" stroke-width="1.6"/></svg>
    <svg class="pointer pointer--two" viewBox="0 0 18 10"><path d="M1 1 L9 5 L1 9 M9 5 H17" fill="none" stroke="#d9427c" stroke-width="1.6"/></svg>

    <ul class="contacts">
      <li>
        <svg viewBox="0 0 12 12"><path d="M3 1 L5 3.5 L4 5 Q5 7 7 8 L8.5 7 L11 9 L9.5 11 Q4 10.5 1 3 Z" fill="#d9427c"/></svg>
        <span>0417 362 958</span>
      </li>
      <li>
        <svg viewBox="0 0 12 12"><rect x="1" y="2.5" width="10" height="7" fill="#d9427c"/><path d="M1 2.5 L6 6.5 L11 2.5" fill="none" stroke="#46445f" stroke-width="1"/></svg>
        <span>fernbrook@qlx.com.au</span>
      </li>
      <li>
        <svg viewBox="0 0 12 12"><path d="M6 11.5 Q2 6.5 2 4.5 A4 4 0 0 1 10 4.5 Q10 6.5 6 11.5 Z" fill="#d9427c"/><circle cx="6" cy="4.5" r="1.4" fill="#46445f"/></svg>
        <span>47 Harlow Parade,<br>Elmsford Vic 3712</span>
      </li>
    </ul>
  </div>

  <div class="patchwork back-patch--bottom" role="img" aria-label="Row of patchwork quilt fabric squares"></div>
</section>

</body>
</html>
```